Website Design for Non-profit

We are looking for a new site design for the Patrons of the Northvale Heritage Hall. The current site can be found at
http://www.patrons-nhh.org/nhhindex_e.html
The URL is provided for reference. We want a completely different look and layout which is shown in the specifications document. Visiting the site, you can learn more about the organization.
Initially, we would like a home page, and inside page provided. Once we a home page and inside page are selected, we would like a simple mobile template provided.
I have attached a full description of the project as well as the specifications document and a zip file containing images for the site.
As mentioned in the specs document, we want to include an image of the museum in the header. The zip file is too large for us to upload (80 meg). The zip file can be obtained by clicking this link:
http://qzl.cc/TrVkWp
The zip file contains several exterior photos and you can select the one you feel is most appropriate to your design.
Updates
Project Deadline Extended
Reason: A long weekend is coming up and a few members of the team are unavailable for review.
Project Deadline Extended
Reason: Reviewing designs. Should have a decision next week.
Project Deadline Extended
Reason: We are discussing the designs and looking to reach a consensus. I will be implementing some designs today or tomorrow. Hopefully final selection will be next week.
Project Deadline Extended
Reason: Still reviewing designs. Hope to get a decision soon.
Project Deadline Extended
Reason: Working to finalize the design. Very close.
Project Deadline Extended
Industry/Entity Type
Museum
Look and feel

```html
<!DOCTYPE html>
<html lang="en">
<head>
<meta charset="utf-8">
<title>Patrons of the Northvale Heritage Hall</title>
<link href="https://fonts.googleapis.com/css2?family=Ubuntu:ital,wght@0,400;0,500;0,700;1,400;1,500&family=Arimo&display=swap" rel="stylesheet">
<style>
:root{
  --page:#ececea;
  --white:#ffffff;
  --gold:#a08a2c;
  --gold-dark:#7d6a1c;
  --gold-light:#bca645;
  --blue:#1d9ccb;
  --blue-dark:#0f7ea8;
  --text:#333333;
  --muted:#555555;
  --link:#2a8fc0;
  --footer:#262626;
  --footer-text:#b9b9b9;
  --line:#dddddd;
  --hero-fill:#8fa9b8;
}
*{margin:0;padding:0;box-sizing:border-box}
html,body{width:960px;height:1200px;overflow:hidden}
body{background:var(--page);font-family:"Ubuntu",sans-serif;color:var(--text);position:relative}
.abs{position:absolute}

/* header */
.site-header{left:0;top:0;width:960px;height:100px;background:linear-gradient(#ffffff,#f1f1f1);border-bottom:2px solid #dedede}
.brand{left:86px;top:24px;display:flex;align-items:center;gap:8px}
.brand-mark{width:22px;height:22px;border-radius:50%;background:var(--gold)}
.brand-name{font-size:20px;font-weight:700;color:var(--gold);letter-spacing:6px}
.top-links{left:408px;top:7px;display:flex;align-items:center;font-size:8.5px;color:#444}
.top-links .social{display:flex;align-items:center;gap:4px;margin-right:10px;font-weight:500;color:#2c4f8f}
.top-links .social i{width:10px;height:10px;background:#2c4f8f;display:inline-block}
.top-links .social.red{color:#c9302c}
.top-links .social.red i{background:#c9302c}
.top-links a{color:#444;text-decoration:none;padding:0 9px;border-left:1px solid #888;line-height:9px}
.top-links a:first-of-type{border-left:none}
.phone{left:636px;top:38px;display:flex;align-items:center;gap:6px}
.phone-icon{width:22px;height:22px;border-radius:4px;background:var(--blue);display:flex;align-items:center;justify-content:center}
.phone-number{font-size:19px;font-weight:500;color:#444;letter-spacing:1px}
.member-badge{background:var(--gold);color:#fff;font-size:8px;padding:4px 6px;border-radius:8px;margin-left:4px}
.font-size{left:534px;top:79px;display:flex;align-items:center;gap:5px;font-size:9px;color:var(--link)}
.font-size b{display:inline-flex;align-items:center;justify-content:center;border:1px solid #9bb;color:var(--link);font-weight:500}
.follow{left:678px;top:76px;display:flex;align-items:center;gap:10px;font-size:15px;color:#444}
.follow .dot{width:24px;height:24px;border-radius:50%;background:linear-gradient(#6fc3e6,#1b7fb4)}

/* hero */
.hero{left:86px;top:120px;width:796px;height:316px;background:var(--white);box-shadow:0 1px 3px rgba(0,0,0,.15)}
.hero-photo{left:8px;top:6px;width:780px;height:302px;background:var(--hero-fill)}

/* nav */
.main-nav{left:82px;top:448px;width:796px;height:35px;border-radius:5px;background:linear-gradient(var(--gold-light),var(--gold) 55%,var(--gold-dark));display:flex;align-items:center;padding-left:16px}
.main-nav a{color:#fff;text-decoration:none;font-size:10.5px;font-weight:500;height:35px;display:flex;align-items:center;padding:0 18px;border-right:1px solid rgba(255,255,255,.3);letter-spacing:.3px}
.main-nav a:last-child{border:none}
.main-nav a.active{background:linear-gradient(#3db4e0,var(--blue-dark));padding:0 14px}

/* tabs */
.tab{height:34px;border-radius:6px 6px 0 0;font-size:11.5px;font-weight:500;display:flex;align-items:center;justify-content:center;color:#333}
.tab.on{background:var(--white);border:1px solid #ddd;border-bottom:none;z-index:2}
.tab.off{background:linear-gradient(#e4e4e4,#d3d3d3)}
.intro{left:82px;top:552px;width:799px;height:211px;background:var(--white);border:1px solid #ddd}
.intro-photo-frame{left:18px;top:22px;width:169px;height:170px;background:#fff;box-shadow:0 0 3px rgba(0,0,0,.25);padding:6px}
.intro-photo{width:100%;height:100%;background:linear-gradient(#b8965a,#3a3632)}
.intro-text{left:208px;top:35px;width:500px;font-size:10.5px;line-height:19.2px;color:#333}
.shadow-l{left:108px;top:763px;width:120px;height:6px;background:radial-gradient(ellipse at top,rgba(0,0,0,.25),transparent 70%)}
.shadow-r{left:730px;top:763px;width:130px;height:6px;background:radial-gradient(ellipse at top,rgba(0,0,0,.25),transparent 70%)}

/* side buttons */
.cta{width:194px;height:47px;display:flex;align-items:center;justify-content:center;color:#fff;font-size:17px;font-weight:700;border:2px solid #fff;box-shadow:0 0 2px rgba(0,0,0,.3)}
.cta.blue{background:linear-gradient(#2fb0df,#0f86b5)}
.cta.gold{background:linear-gradient(#b79e3d,#8c7826)}
.card{background:var(--white);border:1px solid #ddd;border-radius:6px}
.card-title{height:25px;border-radius:4px;background:linear-gradient(#33b3e0,#0f84b2);color:#fff;font-size:14px;display:flex;align-items:center;padding-left:8px}
.card-body{font-size:9px;line-height:13px;color:#333}
.more-btn{right:8px;bottom:8px;background:linear-gradient(#f1ebd3,#d8cca0);color:var(--gold-dark);font-size:10px;font-weight:700;padding:2px 8px;border-radius:8px}

/* news */
.news-item{left:14px;width:344px;height:84px;border-bottom:1px dotted #ccc}
.news-thumb{left:0;top:10px;width:89px;height:60px;box-shadow:0 2px 3px rgba(0,0,0,.25)}
.news-copy{left:100px;top:10px;width:244px;font-size:8.6px;line-height:12.8px;color:#555;text-align:justify}
.news-copy strong{display:block;font-style:italic;font-weight:500;color:#444}
.news-copy .read{color:var(--link);font-style:italic;text-decoration:underline}
.share{right:6px;top:66px;display:flex;gap:5px}
.share span{font-size:6px;padding:1px 4px;border:1px solid #ccc;border-radius:2px}
.share .s1{background:#3c5a96;color:#fff}
.share .s2{background:#f5f5f5;color:var(--link)}

/* footer */
.site-footer{left:0;top:1070px;width:960px;height:130px;background:var(--footer)}
.footer-links{left:98px;top:38px;font-family:"Arimo",sans-serif;font-size:10px;color:var(--footer-text);letter-spacing:.5px;word-spacing:2px}
.footer-info{left:96px;top:76px;font-family:"Arimo",sans-serif;font-size:9.5px;line-height:14.5px;color:var(--footer-text)}
.footer-social{display:inline-flex;gap:4px;vertical-align:middle;margin-left:10px}
.footer-social i{width:14px;height:14px;background:#888;display:inline-block}
.footer-brand{left:662px;top:48px;display:flex;align-items:center;gap:8px;color:#bbb;font-size:9.5px;line-height:11px}
.footer-brand .mark{width:30px;height:30px;background:#777}
</style>
</head>
<body>

<header class="site-header abs">
  <div class="brand abs"><span class="brand-mark"></span><span class="brand-name">PNHH</span></div>
  <nav class="top-links abs">
    <span class="social red"><i></i>ClipHub</span>
    <span class="social"><i></i>Friendbook</span>
    <a>Contact</a><a>Related Sites</a><a>Donate</a><a>Sitemap</a><a>Français</a><a>Member Login</a>
  </nav>
  <div class="phone abs">
    <span class="phone-icon"><svg width="12" height="12" viewBox="0 0 24 24"><path fill="#fff" d="M6.6 10.8a15 15 0 006.6 6.6l2.2-2.2c.3-.3.7-.4 1-.2 1.1.4 2.3.6 3.6.6.6 0 1 .4 1 1V20c0 .6-.4 1-1 1A17 17 0 013 4c0-.6.4-1 1-1h3.5c.6 0 1 .4 1 1 0 1.3.2 2.5.6 3.6.1.3 0 .7-.2 1z"/></svg></span>
    <span class="phone-number">(555) 214 0190</span>
    <span class="member-badge">Not a Member</span>
  </div>
  <div class="font-size abs">Font Size:
    <b style="width:13px;height:13px;font-size:8px">A</b>
    <b style="width:15px;height:15px;font-size:10px;background:var(--blue-dark);color:#fff">A</b>
    <b style="width:15px;height:15px;font-size:11px">A</b>
    <b style="width:17px;height:16px;font-size:13px">A</b>
  </div>
  <div class="follow abs">Follow Us On <span class="dot" title="Friendbook"></span><span class="dot" title="LinkWork"></span><span class="dot" title="Chirper"></span></div>
</header>

<section class="hero abs">
  <div class="hero-photo abs" role="img" aria-label="Exterior photograph of the Northvale Heritage Hall"></div>
</section>

<nav class="main-nav abs">
  <a class="active">Home</a><a>About</a><a>Support PNHH</a><a>Events</a><a>Projects &amp; Programs</a><a>Meet the Friends</a><a>Volunteers</a><a>Publications</a>
</nav>

<div class="tab on abs" style="left:92px;top:518px;width:134px;height:35px">Be a Friend</div>
<div class="tab off abs" style="left:231px;top:518px;width:140px">Be a Donor</div>
<div class="tab off abs" style="left:377px;top:521px;width:136px;height:31px;padding-top:6px">Be a Volunteer</div>

<section class="intro abs">
  <div class="intro-photo-frame abs"><div class="intro-photo" role="img" aria-label="Photograph of three patrons standing together in the hall"></div></div>
  <div class="intro-text abs">
    You are invited to become a friend Help us help the Northvale Heritage Hall to support<br>
    the Museum in its mission to educate,<br>
    preserve and commemorate Canada’s military history.<br><br>
    The friends fulfill our mandate by raising funds for acquisitions and programs,<br>
    providing volunteers in the galleries and conducting special<br>
    events at the Museum.
  </div>
</section>
<div class="shadow-l abs"></div><div class="shadow-r abs"></div>

<div class="cta blue abs" style="left:90px;top:795px">Become a Volunteer</div>
<div class="cta gold abs" style="left:90px;top:859px">Donate Now</div>

<aside class="card abs" style="left:88px;top:923px;width:198px;height:124px">
  <div class="card-title abs" style="left:8px;top:6px;width:182px">Speaker's Bureau</div>
  <p class="card-body abs" style="left:11px;top:42px;width:180px">Lorem Ipsum is simply dummy text of the printing and typesetting industry. Lorem Ipsum has been the industry's standard dummy text....</p>
  <span class="more-btn abs">Chick more »</span>
</aside>

<section class="card abs" style="left:298px;top:794px;width:365px;height:250px">
  <article class="news-item abs" style="top:0">
    <div class="news-thumb abs" role="img" aria-label="Photograph of a jet aircraft on display in a gallery" style="background:#8a93a0"></div>
    <p class="news-copy abs"><strong>Business Communication Headline News:</strong>Find out what’s going on in the world of corporate and business communications. Learn about using communica-tions to better communicate ....<br><span class="read">Contineue Reading</span></p>
    <div class="share abs"><span class="s1">SHARE</span><span class="s2">Post</span></div>
  </article>
  <article class="news-item abs" style="top:84px">
    <div class="news-thumb abs" role="img" aria-label="Photograph of an armoured vehicle in the exhibition hall" style="background:#6b7264"></div>
    <p class="news-copy abs"><strong>Business Communication Headline News:</strong>Find out what’s going on in the world of corporate and business communications. Learn about using communica-tions to better communicate ....<br><span class="read">Contineue Reading</span></p>
    <div class="share abs"><span class="s1">SHARE</span><span class="s2">Post</span></div>
  </article>
  <article class="news-item abs" style="top:168px;border-bottom:none">
    <div class="news-thumb abs" role="img" aria-label="Photograph of two jets flying in a blue sky" style="background:#6aa6d2"></div>
    <p class="news-copy abs"><strong>Business Communication Headline News:</strong>Find out what’s going on in the world of corporate and business communications. Learn about using communica-tions to better communicate ....<br><span class="read">Contineue Reading</span></p>
    <div class="share abs"><span class="s1">SHARE</span><span class="s2">Post</span></div>
  </article>
</section>

<aside class="card abs" style="left:674px;top:788px;width:197px;height:124px">
  <div class="card-title abs" style="left:7px;top:6px;width:183px">Photo Gallery</div>
  <div class="abs" role="img" aria-label="Gallery photograph" style="left:20px;top:53px;width:36px;height:50px;background:#4f6170"></div>
  <div class="abs" role="img" aria-label="Gallery photograph" style="left:140px;top:53px;width:36px;height:50px;background:#3c4a66"></div>
  <div class="abs" role="img" aria-label="Featured gallery photograph of jets in flight" style="left:57px;top:49px;width:84px;height:59px;border:2px solid #fff;box-shadow:0 1px 3px rgba(0,0,0,.3);background:#6aa6d2"></div>
</aside>

<aside class="card abs" style="left:674px;top:920px;width:197px;height:125px">
  <div class="card-title abs" style="left:7px;top:6px;width:183px">Member Treasures</div>
  <div class="abs" role="img" aria-label="Photograph of military medals on display" style="left:10px;top:41px;width:97px;height:45px;background:#8a6536"></div>
  <p class="card-body abs" style="left:114px;top:43px;width:78px;font-size:9.3px">Lorem Ipsum is simply dummy text of the</p>
  <p class="card-body abs" style="left:10px;top:94px;width:182px;font-size:9.3px">printing and typesetting industry. Lorem Ipsum has been ....</p>
</aside>

<footer class="site-footer abs">
  <div class="footer-links abs">Home &nbsp;| &nbsp;About &nbsp;| &nbsp;Support PNHH &nbsp;| &nbsp;Events &nbsp;| &nbsp;Projects &amp; Programs &nbsp;| &nbsp;Meet the Friends &nbsp;| &nbsp;Volunteers</div>
  <div class="footer-info abs">
    Copyright 2013 Patrons of the Northvale Heritage Hall. All Rights Reserved.<br>
    12 Harbour Row, Northvale, Ontario N0V 2H4<br>
    &nbsp;Follow us on : <span class="footer-social"><i></i><i></i><i></i><i></i><i></i></span>
  </div>
  <div class="footer-brand abs">
    <span style="text-align:right">NORTHVALE<br>HERITAGE HALL</span>
    <span class="mark"></span>
    <span>MUSÉE<br>NORTHVALE</span>
  </div>
</footer>

</body>
</html>
```